New Flyer Design Project

Needing brochure explaining the benefits of a home sleep study compared to a clinical hospital sleep study. We had our company logo designed by Lumen Forge, we love it. We would like for it to be a bi-fold. See attachments for examples of information we would like to include.

```html
<!DOCTYPE html>
<html lang="en">
<head>
<meta charset="utf-8">
<title>Prairie Rest Home Sleep Study Brochure</title>
<link rel="stylesheet" href="https://fonts.googleapis.com/css2?family=Montserrat:wght@500;600;700;800;900&family=Roboto:wght@400;500;700&family=Roboto+Condensed:wght@700&display=swap">
<style>
:root{
  --navy:#1b4b87;
  --navy-deep:#143a6d;
  --green:#4bae3c;
  --green-light:#6cc24a;
  --white:#ffffff;
  --ink:#1e2a3a;
  --photo-bed:#c9ccd0;
  --photo-skin:#8d6a55;
  --bg:#ececec;
}
*{margin:0;padding:0;box-sizing:border-box}
html,body{width:814px;height:1200px;overflow:hidden;background:var(--bg)}
body{font-family:"Roboto",Arial,sans-serif;color:var(--ink);position:relative}
.spread{position:absolute;left:0;width:814px;height:577px;overflow:hidden;background:var(--white)}
.spread--outside{top:15px}
.spread--inside{top:608px}
.panel{position:absolute;top:0;width:407px;height:577px;overflow:hidden}
.panel--left{left:0}
.panel--right{left:407px}
.abs{position:absolute}
.wave{position:absolute;left:0;top:0}
.heading{font-family:"Montserrat",Arial,sans-serif;font-weight:800;text-transform:uppercase;line-height:1.12}
.brand{display:flex;align-items:center;gap:8px;font-family:"Montserrat",Arial,sans-serif;font-weight:800;white-space:nowrap}
.brand__dot{width:22px;height:22px;border-radius:50%;flex:none}
.photo{position:absolute;overflow:hidden}

/* outside left: back cover */
.back{background:var(--navy)}
.back__title{left:46px;top:34px;width:320px;font-size:17.5px;color:var(--white)}
.back__lede{left:46px;top:86px;width:290px;font-size:12px;line-height:1.35;color:var(--white)}
.back__rule{left:46px;top:145px;width:140px;height:1px;background:rgba(255,255,255,.8)}
.back__brand{left:48px;top:168px;color:var(--white);font-size:31px}
.back__brand .brand__dot{background:var(--white)}
.back__photo{top:246px;width:152px;height:114px;border:3px solid #cfe0f3;border-radius:4px}
.contact{left:46px;color:var(--white);display:flex;align-items:flex-start;gap:10px}
.contact__icon{width:14px;height:14px;flex:none;margin-top:2px}
.contact--phone{top:382px;font-family:"Montserrat",Arial,sans-serif;font-weight:800;font-size:29px;align-items:center}
.contact--phone .contact__icon{width:18px;height:18px;margin-top:0}
.contact--line{font-size:13px;line-height:1.3}

/* outside right: front cover */
.front__brand{left:58px;top:32px;color:var(--navy);font-size:32px}
.front__brand .brand__dot{background:var(--green)}
.front__photo{left:0;top:96px;width:407px;height:230px}
.front__title{left:44px;top:328px;font-family:"Montserrat",Arial,sans-serif;font-weight:900;font-size:30px;line-height:1.05}
.front__title .l1{color:var(--navy);display:block}
.front__title .l2{color:var(--green);display:block}
.front__sub{left:44px;top:402px;font-size:12.5px;font-weight:500;color:var(--navy-deep)}
.badges{left:44px;top:421px;width:318px;height:50px;background:var(--navy);border-radius:6px;display:flex;align-items:center;padding:0 8px}
.badge{flex:1;display:flex;align-items:flex-start;gap:5px;color:var(--white);font-size:10px;font-weight:700;line-height:1.2;padding:0 6px}
.badge+.badge{border-left:1px solid rgba(255,255,255,.55)}
.tick{width:11px;height:11px;border-radius:50%;background:var(--green);position:relative;flex:none;margin-top:1px}
.tick::after{content:"";position:absolute;left:3.5px;top:2px;width:3px;height:5px;border:solid var(--white);border-width:0 1.6px 1.6px 0;transform:rotate(45deg)}
.front__cta{right:44px;top:549px;font-family:"Montserrat",Arial,sans-serif;font-weight:700;font-size:12.5px;color:var(--white)}

/* inside left */
.intro{background:var(--navy)}
.intro__title{left:46px;top:32px;width:320px;font-size:17.5px;color:var(--white)}
.intro__text{left:46px;width:320px;font-size:11px;line-height:1.35;color:var(--white)}
.checklist{left:28px;top:216px;width:354px;height:262px;background:var(--white);border:2px solid #c7d9ee;border-radius:10px;box-shadow:0 0 0 3px #e8f0f9 inset}
.checklist__bar{position:absolute;left:10px;top:9px;right:10px;height:26px;background:var(--navy);border:2px solid #b8cde8;font-family:"Roboto Condensed",Arial,sans-serif;font-weight:700;font-size:14px;color:var(--white);padding:4px 9px;text-transform:uppercase}
.checklist__ask{position:absolute;left:18px;top:49px;font-family:"Roboto Condensed",Arial,sans-serif;font-weight:700;font-size:12.5px;color:var(--navy-deep)}
.checklist__items{position:absolute;left:22px;top:70px;width:310px;list-style:none}
.checklist__items li{display:flex;gap:11px;font-size:11px;line-height:1.3;color:var(--navy-deep);margin-bottom:9px}
.box{width:15px;height:15px;border:1.5px solid #6f8fb6;border-radius:2px;flex:none}
.checklist__note{position:absolute;left:20px;top:215px;width:300px;font-size:11px;font-weight:700;line-height:1.3;color:var(--navy-deep)}
.inside__brand{left:66px;top:512px;color:var(--navy);font-size:30px}
.inside__brand .brand__dot{background:var(--green)}

/* inside right */
.problem__photo{left:0;top:0;width:407px;height:165px}
.problem__title{left:30px;top:213px;font-family:"Montserrat",Arial,sans-serif;font-weight:900;font-size:18px;color:var(--green)}
.problem__sub{left:30px;top:236px;font-size:12px;font-weight:700;color:var(--navy-deep)}
.problem__text{left:30px;top:256px;width:300px;font-size:11px;line-height:1.3;color:var(--ink)}
.compare{top:317px;width:178px;height:237px;border-radius:8px;padding:12px 10px;color:var(--white)}
.compare--home{left:22px;background:var(--navy)}
.compare--lab{left:214px;background:var(--green)}
.compare__title{font-family:"Roboto Condensed",Arial,sans-serif;font-weight:700;font-size:13.5px;text-transform:uppercase;margin-bottom:16px}
.compare__item{display:flex;gap:5px;margin-bottom:10px}
.compare__item .tick{background:var(--white)}
.compare--home .tick::after{border-color:var(--navy)}
.compare--lab .tick::after{border-color:var(--green)}
.compare__name{font-size:11.5px;font-weight:700;line-height:1.2}
.compare__desc{font-size:8.6px;line-height:1.25;opacity:.95}
.vs{left:192px;top:421px;width:30px;height:30px;border-radius:50%;background:var(--white);border:2px solid var(--navy);font-family:"Montserrat",Arial,sans-serif;font-weight:800;font-size:12px;color:var(--navy);display:flex;align-items:center;justify-content:center}
</style>
</head>
<body>

<!-- Outside spread -->
<section class="spread spread--outside">
  <div class="panel panel--left back">
    <h2 class="abs heading back__title">Sleep apnea test results in less than 72 hours</h2>
    <p class="abs back__lede">Skip the labs, skip the stress, just a simple test at home. $189 with results from board certified sleep physicians</p>
    <div class="abs back__rule"></div>
    <div class="abs brand back__brand"><span class="brand__dot"></span>Prairie Rest</div>
    <div class="photo back__photo" style="left:46px;background:linear-gradient(135deg,#dfe4ea,var(--photo-bed) 60%,#9aa4b0)" role="img" aria-label="Patient asleep wearing sleep study sensors"></div>
    <div class="photo back__photo" style="left:211px;background:linear-gradient(135deg,#e9ecef,#c9a58e 55%,#6d6f73)" role="img" aria-label="Hand wearing a finger pulse oximeter"></div>
    <div class="abs contact contact--phone">
      <svg class="contact__icon" viewBox="0 0 24 24"><path fill="#4bae3c" d="M6.6 10.8a15.1 15.1 0 0 0 6.6 6.6l2.2-2.2a1 1 0 0 1 1-.25 11.4 11.4 0 0 0 3.6.57 1 1 0 0 1 1 1V20a1 1 0 0 1-1 1A17 17 0 0 1 3 4a1 1 0 0 1 1-1h3.5a1 1 0 0 1 1 1c0 1.25.2 2.45.57 3.57a1 1 0 0 1-.25 1z"/></svg>
      555-014-2290
    </div>
    <div class="abs contact contact--line" style="top:422px">
      <svg class="contact__icon" viewBox="0 0 24 24"><circle cx="12" cy="12" r="11" fill="#4bae3c"/><path d="M3 12h18M12 2c3 3 3 17 0 20M12 2c-3 3-3 17 0 20" stroke="#1b4b87" stroke-width="1.6" fill="none"/></svg>
      www.prairierestsleep.com
    </div>
    <div class="abs contact contact--line" style="top:448px">
      <svg class="contact__icon" viewBox="0 0 24 24"><circle cx="12" cy="12" r="11" fill="#4bae3c"/><rect x="6" y="8" width="12" height="8" fill="none" stroke="#1b4b87" stroke-width="1.6"/><path d="M6 8l6 5 6-5" fill="none" stroke="#1b4b87" stroke-width="1.6"/></svg>
      hello@prairierestsleep.com
    </div>
    <div class="abs contact contact--line" style="top:474px;width:300px">
      <svg class="contact__icon" viewBox="0 0 24 24"><path fill="#4bae3c" d="M12 1a8 8 0 0 0-8 8c0 6 8 14 8 14s8-8 8-14a8 8 0 0 0-8-8zm0 11a3 3 0 1 1 0-6 3 3 0 0 1 0 6z"/></svg>
      218 Linden Row, Suite 40, Cedar Falls, IA 50613
    </div>
    <svg class="wave" width="407" height="577" viewBox="0 0 407 577">
      <path d="M0 512 C120 540 260 538 407 495 L407 577 L0 577Z" fill="#ffffff"/>
      <path d="M0 524 C130 552 270 548 407 508 L407 577 L0 577Z" fill="#4bae3c"/>
    </svg>
  </div>

  <div class="panel panel--right">
    <div class="abs brand front__brand"><span class="brand__dot"></span>Prairie Rest</div>
    <div class="photo front__photo" style="background:linear-gradient(120deg,#8c949e,#d6d8da 45%,#eef0f1 70%,#b9bec4)" role="img" aria-label="Man sleeping on a couch wearing a CPAP mask"></div>
    <svg class="wave" width="407" height="577" viewBox="0 0 407 577">
      <path d="M0 300 C90 262 240 262 407 232 L407 330 L0 330Z" fill="#4bae3c"/>
      <path d="M0 308 C100 272 250 275 407 248 L407 330 L0 330Z" fill="#1b4b87"/>
      <path d="M0 322 C110 290 260 292 407 268 L407 330 L0 330Z" fill="#ffffff"/>
      <path d="M0 560 C150 540 280 522 407 500 L407 577 L0 577Z" fill="#1b4b87"/>
      <path d="M0 566 C150 548 280 532 407 512 L407 577 L0 577Z" fill="#4bae3c"/>
    </svg>
    <h1 class="abs front__title"><span class="l1">Better Sleep</span><span class="l2">Starts At Home</span></h1>
    <p class="abs front__sub">Simple. Comfortable. Accurate Home Sleep Study.</p>
    <div class="abs badges">
      <div class="badge"><span class="tick"></span><span>FDA Cleared Device, DOT Approved.</span></div>
      <div class="badge"><span class="tick"></span><span>Results in less than 72 Hours</span></div>
      <div class="badge"><span class="tick"></span><span>98 Percent Lab Accuracy</span></div>
    </div>
    <p class="abs front__cta">Order Your Home Sleep Study Today</p>
  </div>
</section>

<!-- Inside spread -->
<section class="spread spread--inside">
  <div class="panel panel--left">
    <svg class="wave" width="407" height="577" viewBox="0 0 407 577">
      <path d="M0 0 H407 V232 C300 238 180 250 0 262Z" fill="#1b4b87"/>
    </svg>
    <h2 class="abs heading intro__title">80% of sleep apneacases go undiagnosed.</h2>
    <p class="abs intro__text" style="top:86px">You wake up exhausted. You fall asleep at your desk. Your partner says you stop breathing at night. You know something's wrong.</p>
    <p class="abs intro__text" style="top:141px">Most people wait years before getting tested because sleep labs are expensive, inconvenient, and scheduled months out. Meanwhile you're crashing your car, destroying your health, and feeling like garbage every single day.</p>
    <div class="abs checklist">
      <div class="checklist__bar">Self Assessment Checklist</div>
      <p class="checklist__ask">DO YOU</p>
      <ul class="checklist__items">
        <li><span class="box"></span>Snore loudly?</li>
        <li><span class="box"></span>Wake up gasping or choking?</li>
        <li><span class="box"></span>Fall asleep during the day even when you slept 8 hours?</li>
        <li><span class="box"></span>Wake up with headaches?</li>
        <li><span class="box"></span>Feel tired no matter how much you sleep?</li>
      </ul>
      <p class="checklist__note">If you checked 2 boxes, you probably have sleep apnea. Stop guessing. Get tested.</p>
    </div>
    <div class="abs brand inside__brand"><span class="brand__dot"></span>Prairie Rest</div>
  </div>

  <div class="panel panel--right">
    <div class="photo problem__photo" style="background:linear-gradient(110deg,#cfd1d3,#eceeef 45%,#7a5c4c 60%,#e4e6e8 80%)" role="img" aria-label="Hospital patient's hand with IV line and pulse sensor on bed sheets"></div>
    <svg class="wave" width="407" height="577" viewBox="0 0 407 577">
      <path d="M0 160 C120 130 270 140 407 108 L407 200 L0 200Z" fill="#4bae3c"/>
      <path d="M0 168 C130 142 280 150 407 122 L407 200 L0 200Z" fill="#1b4b87"/>
      <path d="M0 182 C140 158 290 166 407 142 L407 200 L0 200Z" fill="#ffffff"/>
    </svg>
    <h2 class="abs problem__title">THE PROBLEM</h2>
    <p class="abs problem__sub">Sleep care wasn't built with people in mind.</p>
    <p class="abs problem__text">Most people wait months, spend a fortune and end up feeling more like a chart than a human. It doesn't have to be this way.</p>

    <div class="abs compare compare--home">
      <h3 class="compare__title">Home Sleep Study</h3>
      <div class="compare__item"><span class="tick"></span><div><p class="compare__name">Comfortable</p><p class="compare__desc">A minimal device with 2 wires and 3 sensors</p></div></div>
      <div class="compare__item"><span class="tick"></span><div><p class="compare__name">Convenient</p><p class="compare__desc">Delivered to your door - sleep in your own bed at home</p></div></div>
      <div class="compare__item"><span class="tick"></span><div><p class="compare__name">Accessible</p><p class="compare__desc">Scheduling and device delivery in 2 - 4 business days</p></div></div>
      <div class="compare__item"><span class="tick"></span><div><p class="compare__name">Affordable</p><p class="compare__desc">Pay a one-time flat fee of $189</p></div></div>
    </div>
    <div class="abs compare compare--lab">
      <h3 class="compare__title">In-Lab Testing</h3>
      <div class="compare__item"><span class="tick"></span><div><p class="compare__name">Invasive</p><p class="compare__desc">20-30 wires attached all over your body</p></div></div>
      <div class="compare__item"><span class="tick"></span><div><p class="compare__name">Disruptive</p><p class="compare__desc">Must sleep in a lab overnight and requires travel</p></div></div>
      <div class="compare__item"><span class="tick"></span><div><p class="compare__name">Hard to schedule</p><p class="compare__desc">Scheduling can take anywhere from 3 weeks to 6 months</p></div></div>
      <div class="compare__item"><span class="tick"></span><div><p class="compare__name">Expensive</p><p class="compare__desc">Fees can range from $500 - $10,000</p></div></div>
    </div>
    <div class="abs vs">VS</div>
  </div>
</section>

</body>
</html>
```